Creation d’une etiquette pour pots de confiture d’orange
Besoins
Nous souhaitons une étiquettes design sur fond transparent.
Nous cultivons des oranges en Sardaigne et voulons commercialiser une confiture artisanale faite à la main.
La marque de la confiture serait éventuellement ''Corsetta''
Les messages que nous voulons passer sont :
- fraicheur: confiture faite avec les fruits de saison à peine cueillis
- circuit court: confiture faite par le planteur
- Etiquette à faire avec slogans en Italien
- Sardaigne: oasis écologique
- made in italy avec drapeau italien
Public visé : épicerie fine, vente internet et vente privée
Pot vertical cylindre de h110x73 mm avec couvercle noir
On serait ravis de travailler avec vous ;)
N'hésitez pas à nous contacter pour d'autres info
Baptiste et Marie-Solène
Description de l'entreprise
Entreprise familiale agricole en Sardaigne
La cible
épiceries fines, ventes privées, ventes internet
Couleurs, favoris et autres exigences:
-Orange, Vert
-Vert blanc rouge

```html
<!DOCTYPE html>
<html lang="it">
<head>
<meta charset="utf-8">
<title>Corsetta – Marmellata di Arance</title>
<link href="https://fonts.googleapis.com/css2?family=Barlow:wght@400;500;700&display=swap" rel="stylesheet">
<style>
  :root {
    --jam: #f5b324;
    --jam-light: #f9c94a;
    --orange: #f38a22;
    --orange-deep: #e2651b;
    --ink: #2f3a30;
    --flag-green: #2e8b3d;
    --flag-white: #f6f3ea;
    --flag-red: #c8322b;
  }
  * { margin: 0; padding: 0; box-sizing: border-box; }
  html, body {
    width: 827px;
    height: 1200px;
    overflow: hidden;
  }
  body {
    background: radial-gradient(ellipse at 50% 45%, var(--jam-light), var(--jam) 70%);
    font-family: "Barlow", Arial, sans-serif;
    color: var(--ink);
    position: relative;
  }
  .label {
    position: absolute;
    left: 70px;
    top: 250px;
    width: 690px;
    height: 700px;
  }
  .illustration {
    position: absolute;
    left: 90px;
    top: 70px;
    width: 420px;
    height: 420px;
    border-radius: 50%;
    background: radial-gradient(circle at 45% 40%, var(--orange) 0%, var(--orange-deep) 100%);
  }
  .brand {
    position: absolute;
    right: 40px;
    top: 0;
    font-size: 34px;
    font-weight: 500;
    letter-spacing: 0.28em;
    text-transform: uppercase;
    line-height: 44px;
  }
  .frame {
    position: absolute;
    left: 430px;
    top: 0;
  }
  .info-row {
    position: absolute;
    left: 0;
    top: 545px;
    width: 690px;
    display: flex;
    justify-content: space-between;
    align-items: flex-start;
  }
  .product {
    font-size: 22px;
    line-height: 1.3;
    letter-spacing: 0.18em;
  }
  .product .fruit {
    font-size: 34px;
    font-weight: 700;
    letter-spacing: 0.12em;
  }
  .origin-badge {
    display: flex;
    flex-direction: column;
    align-items: center;
    gap: 8px;
    margin-top: 10px;
  }
  .origin-badge .made {
    font-size: 16px;
    letter-spacing: 0.02em;
  }
  .claim {
    font-size: 26px;
    line-height: 1.2;
    letter-spacing: 0.22em;
    text-align: left;
  }
</style>
</head>
<body>
  <section class="label">
    <div class="illustration" role="img" aria-label="Illustrazione di un'arancia intera e di uno spicchio tagliato con foglia verde"></div>

    <svg class="frame" width="260" height="520" viewBox="0 0 260 520" aria-hidden="true">
      <polyline points="250,40 258,40 258,500 150,500" fill="none" stroke="var(--ink)" stroke-width="2"/>
    </svg>
    <h1 class="brand">Corsetta</h1>

    <div class="info-row">
      <p class="product">Marmellata<br><span class="fruit">ARANCE</span><br>Sardegna</p>

      <div class="origin-badge">
        <svg width="96" height="64" viewBox="0 0 96 64" aria-label="Bandiera italiana" role="img">
          <rect x="0" y="0" width="32" height="64" fill="var(--flag-green)"/>
          <rect x="32" y="0" width="32" height="64" fill="var(--flag-white)"/>
          <rect x="64" y="0" width="32" height="64" fill="var(--flag-red)"/>
        </svg>
        <span class="made">made in Italy</span>
      </div>

      <p class="claim">Produzione<br>locale<br>artigianale</p>
    </div>
  </section>
</body>
</html>
```